K.E.M.A. The Quillan Orchard Papers

This is the cover artwork for the audio version
of the re-creation of the Quillan Orchard Papers based around the killing of Dorian Vatts. I need a cover for the library binders. I have the template for the binder that I can send. The title of the audio is: K.E.M.A. I would like the words Quillan Orchard Papers added in somehow with some creative graphics. I have a website with other audio covers. I also need the words: Unabridged CD format somewhere at the bottom. Can I send the binder template later?

Target Market(s)

Audiobook

Industry/Entity Type

Audio

Font styles to use
Serif

Requirements
Nice to have
• no bullets, no blood, no dead bodies, no police, no police cars, no protest, no
• violent images, no bullets
Should not have
• nice clear sleek look

```html
<!DOCTYPE html>
<html lang="en">
<head>
<meta charset="UTF-8">
<title>K.E.M.A. – The Quillan Orchard Papers</title>
<link rel="stylesheet" href="https://fonts.googleapis.com/css2?family=Tinos:ital,wght@0,400;0,700;1,700&display=swap">
<style>
  :root {
    --bg-light: #dc9566;
    --bg-mid: #c9733f;
    --bg-dark: #a9542a;
    --ink: #58322a;
    --white: #ffffff;
    --gold: #f2b705;
  }
  * { margin: 0; padding: 0; box-sizing: border-box; }
  html, body { width: 1200px; height: 1200px; overflow: hidden; }
  body { font-family: "Tinos", "Times New Roman", serif; }

  .cover {
    position: relative;
    width: 1200px;
    height: 1200px;
    overflow: hidden;
    background:
      repeating-linear-gradient(90deg, rgba(90,40,15,0.05) 0 2px, rgba(255,220,190,0.03) 2px 5px, rgba(90,40,15,0.04) 5px 9px),
      radial-gradient(ellipse 55% 50% at 50% 55%, var(--bg-light) 0%, var(--bg-mid) 60%, var(--bg-dark) 100%);
  }

  .frame {
    position: absolute;
    left: 48px; top: 48px;
    width: 1104px; height: 1104px;
    border: 2.5px solid var(--white);
  }

  .series {
    position: absolute;
    top: 180px; left: 0; width: 100%;
    text-align: center;
    font-weight: 700;
    font-size: 112px;
    line-height: 1;
    color: var(--ink);
  }
  .series .dot { color: var(--white); }

  .series-rule {
    position: absolute;
    top: 188px;
    width: 2.5px; height: 110px;
    background: var(--white);
  }
  .series-rule.left { left: 357px; }
  .series-rule.right { left: 841px; }

  .title-line {
    position: absolute;
    right: 220px;
    line-height: 1;
    color: var(--ink);
    white-space: nowrap;
  }
  .title-top {
    top: 462px;
    font-size: 128px;
    font-weight: 700;
    letter-spacing: 20px;
    margin-right: -20px;
  }
  .title-middle {
    top: 586px;
    font-size: 56px;
    font-weight: 400;
    letter-spacing: 42px;
    margin-right: -42px;
  }
  .title-bottom {
    top: 646px;
    font-size: 104px;
    font-weight: 700;
    letter-spacing: 24px;
    margin-right: -24px;
  }
  .title-initial {
    position: absolute;
    left: 330px;
    top: 578px;
    font-size: 230px;
    font-weight: 700;
    font-style: italic;
    line-height: 1;
    color: var(--white);
  }

  .gold-rule {
    position: absolute;
    left: 478px; top: 1045px;
    width: 268px; height: 3px;
    background: var(--gold);
  }

  .format {
    position: absolute;
    top: 1080px; left: 0; width: 100%;
    text-align: center;
    font-size: 22px;
    font-weight: 700;
    line-height: 1;
    color: var(--white);
    letter-spacing: 0.5em;
    word-spacing: 1.4em;
  }
</style>
</head>
<body>
  <main class="cover">
    <div class="frame"></div>

    <span class="series-rule left"></span>
    <h2 class="series">K<span class="dot">.</span>E<span class="dot">.</span>M<span class="dot">.</span>A<span class="dot">.</span></h2>
    <span class="series-rule right"></span>

    <h1 class="title" aria-label="Quillan Orchard Papers">
      <span class="title-line title-top">QUILLAN</span>
      <span class="title-line title-middle">Orchard</span>
      <span class="title-initial">P</span>
      <span class="title-line title-bottom">APERS</span>
    </h1>

    <div class="gold-rule"></div>
    <p class="format">Unabridged CD format</p>
  </main>
</body>
</html>
```